Security Business card

I need a new business card for my new company Bastion Crest Security Group we provide security for clubs,pubs,hotels etc. I would like to see the main colors red and black to be used. The final design should communicate honor and integrity.

Industry/Entity Type

Security

Contact Information for Business Card

Marcus Delvane
Company Name-Bastion Crest Security Group
Abn-47318265094
Acn-318265094
address- po box 7352 Ferndale nsw 2291
phone- 0437682915
email- Marcus@bastioncrest.com.au

```html
<!DOCTYPE html>
<html lang="en">
<head>
<meta charset="utf-8">
<title>Bastion Crest Security Group – Business Card</title>
<link rel="stylesheet" href="https://fonts.googleapis.com/css2?family=Open+Sans:ital,wght@0,400;0,700;1,700&display=swap">
<style>
  :root {
    --crest-red: #e0192f;
    --ink-black: #050505;
    --paper-white: #ffffff;
    --backdrop: #d9d9d9;
  }
  html, body {
    margin: 0;
    padding: 0;
    width: 1200px;
    height: 900px;
    overflow: hidden;
    background: var(--backdrop);
  }
  .business-card {
    position: absolute;
    left: 75px;
    top: 150px;
    width: 1050px;
    height: 600px;
    font-family: "Open Sans", Arial, sans-serif;
    color: var(--paper-white);
    box-shadow: 0 10px 30px rgba(0,0,0,0.25);
    overflow: hidden;
  }
  .card-shapes {
    position: absolute;
    inset: 0;
  }
  .brand-mark {
    position: absolute;
    left: 60px;
    top: 40px;
    width: 300px;
    display: flex;
    flex-direction: column;
    align-items: center;
  }
  .brand-circle {
    width: 170px;
    height: 170px;
    border: 10px solid var(--paper-white);
    border-radius: 50%;
    box-sizing: border-box;
  }
  .brand-name {
    margin-top: 22px;
    font-weight: 700;
    font-size: 28px;
    letter-spacing: 1px;
    text-transform: uppercase;
    color: var(--paper-white);
  }
  .company-name {
    position: absolute;
    right: 40px;
    top: 128px;
    margin: 0;
    font-weight: 700;
    font-size: 34px;
    text-transform: uppercase;
    white-space: nowrap;
  }
  .contact-block {
    position: absolute;
    right: 70px;
    top: 290px;
    text-align: right;
  }
  .person-name {
    margin: 0 0 48px;
    font-weight: 700;
    font-style: italic;
    font-size: 40px;
  }
  .contact-line {
    margin: 0;
    font-weight: 400;
    font-size: 28px;
    line-height: 46px;
  }
</style>
</head>
<body>
  <div class="business-card">
    <svg class="card-shapes" viewBox="0 0 1050 600" width="1050" height="600" aria-hidden="true">
      <rect class="card-base" x="0" y="0" width="1050" height="600" fill="var(--crest-red)"/>
      <polygon class="top-panel-rule" points="486,0 1050,0 1050,104 458,104" fill="var(--paper-white)"/>
      <polygon class="top-panel" points="502,0 1050,0 1050,96 476,96" fill="var(--ink-black)"/>
      <polygon class="lower-panel-rule" points="430,205 1050,205 1050,600 255,600" fill="var(--paper-white)"/>
      <polygon class="lower-panel" points="448,217 1050,217 1050,600 274,600" fill="var(--ink-black)"/>
    </svg>

    <div class="brand-mark">
      <div class="brand-circle"></div>
      <div class="brand-name">Bastion Crest</div>
    </div>

    <h1 class="company-name">Bastion Crest Security Group</h1>

    <div class="contact-block">
      <p class="person-name">Marcus Delvane</p>
      <p class="contact-line">Adress: 3po box 7352 Ferndale nsw 2291</p>
      <p class="contact-line">Phone: 0437682915</p>
      <p class="contact-line">Email: Marcus@bastioncrest.com.au</p>
    </div>
  </div>
</body>
</html>
```